New webdesign for a cable company

We need a new design for Lumo Nett.

There exist a suggestion for the page, were we have attached files to show you this. The design here is not good enough, but here you can se what content we need.

You can feel free to give adjustment to this design to make it better, our blow us away with a new brilliant design, but from this design you see what content we need.

The important is that the company get a design who represent its products:
- TV = Cable TV
- Bredbånd = Broadband
- Mobil = Mobile phone
- Strøm = Electricity
- Alarm = Alarm
- Lumo Samlet = a cobain pagage of all our products.

Lumo Nett would like costumers who visit the site to het the impression that Lumo Nett is a professional, innovative and fun company.
Updates

We have to day uploaded pictures of the existing page as the link haven't been working for the most of you as it's placed on a server our developer are using and is often shut it down. 

We have also updated the brief with some new and updated description so please read true the updated brief. 

We will at the same time inform that we haven't been able to give feedback on any of the received design and are sorry for that, we will within the next 24 hours hopefully have started responded the different received designs.

Looking forward to see more suggestion and hope you will help us create and very professional and informative design. 

Reason: We have decided to extend the deadline due to the number of design suggestion who is sent in and your lack of response to all designers due to our own workload.

This project was unfortunately for different reason put on ice for a while, but we are now ready to complete the design and will answer and give feedback too all the received design suggestions. 

Within a couple of days we hope we have answered all you who sent us suggestions, we appreciate all suggestions and hope to get in more suggestions.

Reason: Deisgn description have been updated

Target Market(s)

Our costumer are both private and companies

Industry/Entity Type

Tv

Requirements
Must have
• A easy way to promote and inform about changes in our products, there are a constant change in our products and it must bee a easy and good way to changes ass the marked change. Cheek out this link, for a example of what we like/think of here, https://kabel.fjordvisjon.no

On all pages there must be a easy way to click on a order button and too inform about your interest (thats two different things), could be placed in the top right corner for example. In the order form you should follow a step by step part:
1. Cheek what product we can provide you.
2. Chooce products.
3. Costumer inforamtion.
4. Confirmation.

Somewere on the portal it must be possible for costumers to log on to their own administration, where they can cheek for invoices, other statuses, etc.

A main menu existing of:
Hjem (Home)
Produkter (Products)
Storkunde (key account/large costumers)
Kundeservice (Costumerservice)
Min side (My page)

The main menu should have the following sub titles:
- Under "Produkter"/products our different products must be listed
- Under "Kundeservice"/Costumerservice it must have these submenus:
- Hjelp og støtte = Help.
- Faktura = Invoice
- Brukerguider = Userguides
- Abbonementavtaler = Terms and conditions.

A bottom menu where we have 5 main categories, with sub categories:
Om oss (about us)
- Om Lumo Nett (about Lumo Nett)
- Kontaktinformajson ( contact information)
- Pressemeldinger (Pressrelese)
- Ledige stillinger (positions available)
- KRAB ( and organisastion in our field)

Produkter (Product)
- TV (TV)
- Bredbånd (Broadand)
- Telefoni (telephony, both mobil)
- Strøm (elecricity)
- Arlam (Alarm)

Borrettslag/Sameier (Housing cooperatives)
- Løsninger (solutions)
- Produkter (product)
- Kontaktpersoner (contactpersons)

Utbygger (developer)
- Hva vi kan gjøre for dere. (What we can do for you)

Opperatørnett (operators)

Build up the categories and bottom menu something like this:
https://kabel.fjordvisjon.no
www.brenvik.com
Nice to have
• A main menu existing of:
Hjem (Home)
Produkter (Products)
Lumo Nett
Kontakt oss (Contact us)

Under "Produkter"/products our different products must be listed and under "Kundeservice"/Costumerservice it must have these submenus:
- Hjelp og støtte = Help.
- Faktura = Invoice
Should not have
• Any translation section since the homepage only will be in Norwegian.

```html
<!DOCTYPE html>
<html lang="no">
<head>
<meta charset="utf-8">
<title>Lumo Nett – Bredbånd</title>
<link rel="stylesheet" href="https://fonts.googleapis.com/css2?family=Ubuntu:wght@400;500&family=Arimo:ital,wght@0,400;0,700;1,700&display=swap">
<style>
  :root {
    --bar-black: #050505;
    --page-grey: #ececec;
    --panel-white: #ffffff;
    --ink: #333333;
    --ink-soft: #8a8a8a;
    --ink-muted: #9a9a9a;
    --accent-blue: #2f6eb5;
    --frame-line: #e2e2e2;
    --footer-dark: #1a1a1a;
    --footer-text: #a8a8a8;
  }
  * { box-sizing: border-box; margin: 0; padding: 0; }
  html, body { width: 1200px; height: 1012px; overflow: hidden; }
  body {
    position: relative;
    background: linear-gradient(#eeeeee, #e6e6e6);
    font-family: "Arimo", Arial, sans-serif;
    color: var(--ink);
  }
  .abs { position: absolute; }

  /* top bar */
  .top-bar { left: 0; top: 0; width: 1200px; height: 37px; background: var(--bar-black); }
  .social-links { left: 183px; top: 12px; display: flex; gap: 4px; }
  .social-links span { width: 12px; height: 12px; border-radius: 2px; background: #5b7fb6; }
  .social-links span:first-child { background: #e58b2a; }
  .social-links span:nth-child(3) { background: #d9d9d9; }
  .social-links span:nth-child(4) { background: #4ba8d8; }
  .social-links span:nth-child(6) { background: #d9d9d9; }
  .quick-actions { left: 560px; top: 8px; display: flex; gap: 8px; }
  .quick-actions a {
    display: block; height: 21px; padding: 0 10px; line-height: 21px;
    font-size: 10px; font-weight: 700; color: #fff; text-decoration: none; border-radius: 2px;
  }
  .order-button { background: var(--accent-blue); }
  .interest-button { border: 1px solid #555; color: #ddd !important; line-height: 19px !important; }
  .search-label { left: 778px; top: 12px; font-size: 10px; color: #cfcfcf; }
  .search-box {
    left: 841px; top: 6px; width: 177px; height: 26px; background: #fff;
    border: 1px solid #cfcfcf; font-size: 10px; color: #aaa; padding: 6px 8px;
  }
  .search-box svg { position: absolute; right: 8px; top: 8px; }

  /* header */
  .site-header { left: 0; top: 37px; width: 1200px; height: 77px; background: var(--panel-white); }
  .brand { left: 172px; top: 22px; display: flex; align-items: center; gap: 12px; }
  .brand-dot { width: 28px; height: 28px; border-radius: 50%; background: var(--accent-blue); }
  .brand-name { font-family: "Ubuntu", sans-serif; font-size: 31px; color: #4a4a4a; }
  .main-nav { right: 195px; top: 61px; display: flex; gap: 22px; font-family: "Ubuntu", sans-serif; text-align: center; }
  .main-nav a { position: relative; text-decoration: none; }
  .main-nav b { display: block; font-weight: 400; font-size: 14px; color: #2d2d2d; white-space: nowrap; }
  .main-nav small { display: block; font-family: "Arimo", sans-serif; font-size: 9.5px; color: var(--ink-muted); margin-top: 2px; white-space: nowrap; }
  .main-nav .is-current::before {
    content: ""; position: absolute; left: -6px; right: -6px; top: -24px; height: 5px; background: var(--accent-blue);
  }
  .main-nav .is-current::after {
    content: ""; position: absolute; left: 50%; margin-left: -5px; top: -19px;
    border: 5px solid transparent; border-top-color: var(--accent-blue);
  }

  /* product sub nav */
  .product-tabs { top: 141px; font-family: "Ubuntu", sans-serif; font-size: 12px; color: #333; letter-spacing: 0.3px; }
  .product-tabs.is-active { color: var(--accent-blue); }

  /* thumbnails */
  .thumb { top: 182px; width: 200px; height: 137px; background: #fff; border: 1px solid var(--frame-line); padding: 8px; }
  .thumb div { width: 100%; height: 100%; }
  .thumb-cables div { background: linear-gradient(135deg, #3a2b22, #1b1a19 55%, #d8d4cc); }
  .thumb-fibre div { background: radial-gradient(circle at 60% 50%, #37d27a, #0f8fb0 55%, #083a55); }
  .thumb-phone div { background: linear-gradient(160deg, #e4e4e4, #8a8a8a 45%, #2a2a2a 70%, #bdbdbd); }
  .thumb-router div { background: linear-gradient(90deg, #d7d7d7, #1c1c1c 40%, #303030 60%, #e3e3e3); }

  /* detail panel */
  .detail-pointer { left: 898px; top: 334px; border: 11px solid transparent; border-bottom-color: #fff; border-top: 0; }
  .detail-panel { left: 186px; top: 344px; width: 824px; height: 440px; background: var(--panel-white); border: 1px solid #e8e8e8; }
  .close-mark { left: 991px; top: 349px; font-size: 13px; color: #555; }
  .product-photo { left: 212px; top: 376px; width: 384px; height: 370px; background: radial-gradient(ellipse at 55% 45%, #4a4a4a 0%, #1e1e1e 25%, #9a9a9a 45%, #dcdcdc 80%); }
  .pager { top: 711px; height: 22px; font-size: 9px; display: flex; align-items: center; justify-content: center; background: #fff; border: 1px solid #ddd; color: #333; }
  .pager.is-current { background: #111; color: #fff; border-color: #111; }

  .detail-title { left: 630px; top: 376px; font-size: 12px; font-weight: 700; font-style: italic; color: #555; }
  .detail-body { left: 630px; top: 413px; width: 330px; font-size: 10px; line-height: 17px; color: var(--ink-soft); }
  .detail-list { left: 624px; width: 340px; font-size: 10px; color: #7c7c7c; }
  .select-button {
    left: 930px; top: 673px; width: 73px; height: 35px; background: #f0f0f0;
    border: 1px solid #dcdcdc; font-size: 10.5px; color: #333; text-align: center; line-height: 33px;
  }
  .price { left: 900px; top: 722px; width: 103px; text-align: right; font-size: 18px; color: #222; }

  /* order steps */
  .order-steps { left: 186px; top: 800px; width: 824px; height: 34px; display: flex; }
  .order-steps li {
    flex: 1; list-style: none; display: flex; align-items: center; gap: 8px;
    font-size: 11px; color: #666; padding-left: 14px; border-right: 1px solid #dcdcdc; background: #f6f6f6;
  }
  .order-steps li:last-child { border-right: 0; }
  .order-steps span {
    width: 18px; height: 18px; border-radius: 50%; background: #bbb; color: #fff;
    font-size: 10px; font-weight: 700; text-align: center; line-height: 18px;
  }
  .order-steps .is-current span { background: var(--accent-blue); }
  .order-steps .is-current { color: #222; font-weight: 700; }

  /* footer */
  .site-footer { left: 0; top: 850px; width: 1200px; height: 162px; background: var(--footer-dark); }
  .footer-menu { left: 186px; top: 16px; width: 824px; display: flex; justify-content: space-between; }
  .footer-menu h4 { font-family: "Ubuntu", sans-serif; font-weight: 500; font-size: 12px; color: #fff; margin-bottom: 7px; }
  .footer-menu li { list-style: none; font-size: 10.5px; line-height: 17px; color: var(--footer-text); }
</style>
</head>
<body>
  <div class="abs top-bar"></div>
  <div class="abs social-links" aria-label="Sosiale medier"><span></span><span></span><span></span><span></span><span></span><span></span></div>
  <div class="abs quick-actions">
    <a class="order-button" href="#bestill">Bestill</a>
    <a class="interest-button" href="#interesse">Meld interesse</a>
  </div>
  <div class="abs search-label">Site Search:</div>
  <div class="abs search-box">Search:
    <svg width="6" height="9" viewBox="0 0 6 9"><path d="M0 0 L6 4.5 L0 9Z" fill="#333"/></svg>
  </div>

  <header class="abs site-header">
    <div class="abs brand"><span class="brand-dot"></span><span class="brand-name">Lumo Nett</span></div>
  </header>
  <nav class="abs main-nav">
    <a href="#"><b>HJEM</b><small>Til forsiden</small></a>
    <a href="#" class="is-current"><b>PRODUKTER</b><small>TV, bredbånd, mobil</small></a>
    <a href="#"><b>STORKUNDE</b><small>For bedrifter</small></a>
    <a href="#"><b>KUNDESERVICE</b><small>Hjelp og faktura</small></a>
    <a href="#"><b>MIN SIDE</b><small>Logg inn</small></a>
  </nav>

  <div class="abs product-tabs" style="left:186px">PRODUCT 1</div>
  <div class="abs product-tabs" style="left:279px">PRODUCT 2</div>
  <div class="abs product-tabs" style="left:373px">MOBILE PRODUCT</div>
  <div class="abs product-tabs is-active" style="left:496px">BROADBAND&nbsp; PRODUCT</div>

  <div class="abs thumb thumb-cables" style="left:185px"><div role="img" aria-label="Cables plugged into the back of a receiver"></div></div>
  <div class="abs thumb thumb-fibre" style="left:393px"><div role="img" aria-label="Green network cable among glowing fibre optics"></div></div>
  <div class="abs thumb thumb-phone" style="left:602px"><div role="img" aria-label="Smartphone lying on a surface"></div></div>
  <div class="abs thumb thumb-router" style="left:810px"><div role="img" aria-label="Black upright broadband router"></div></div>

  <div class="abs detail-panel"></div>
  <div class="abs detail-pointer"></div>
  <div class="abs close-mark">x</div>
  <div class="abs product-photo" role="img" aria-label="Black upright broadband router on a grey studio background"></div>
  <div class="abs pager is-current" style="left:508px;width:23px">1</div>
  <div class="abs pager" style="left:534px;width:20px">2</div>
  <div class="abs pager" style="left:559px;width:22px">&gt;&gt;</div>

  <div class="abs detail-title">Lorem ipsum dolor sit amet, consectetur adipiscing elit.</div>
  <p class="abs detail-body">Pellentesque diam mi, dapibus non bibendum at, bibendum ac neque. Sed at leo arcu. Ut at diam et sem convallis tempor. Fusce a metus eget purus convallis pulvinar et ut felis. In elementum massa eu diam auctor tincidunt. Pellentesque habitant morbi tristique senectus et netus et malesuada fames ac turpis egestas.</p>
  <p class="abs detail-list" style="top:520px">- Phasellus sed enim justo, ac adipiscing dui.</p>
  <p class="abs detail-list" style="top:554px">- Maecenas ut justo nec - dui fermentum lacinia. Nunc volutpat sem.</p>
  <p class="abs detail-list" style="top:589px">- Suspendisse viverra diam sit amet felis congue et aliquet neque.</p>
  <p class="abs detail-list" style="top:623px">- pretium. Praesent at mi est. Cras ac tortor leo.</p>
  <div class="abs select-button">Select</div>
  <div class="abs price">$ 199.90</div>

  <ol class="abs order-steps" aria-label="Bestilling steg for steg">
    <li class="is-current"><span>1</span>Sjekk hva vi kan levere</li>
    <li><span>2</span>Velg produkter</li>
    <li><span>3</span>Kundeinformasjon</li>
    <li><span>4</span>Bekreftelse</li>
  </ol>

  <footer class="abs site-footer">
    <div class="abs footer-menu">
      <div>
        <h4>Om oss</h4>
        <ul><li>Om Lumo Nett</li><li>Kontaktinformasjon</li><li>Pressemeldinger</li><li>Ledige stillinger</li><li>KRAB</li></ul>
      </div>
      <div>
        <h4>Produkter</h4>
        <ul><li>TV</li><li>Bredbånd</li><li>Telefoni</li><li>Strøm</li><li>Alarm</li></ul>
      </div>
      <div>
        <h4>Borettslag/Sameier</h4>
        <ul><li>Løsninger</li><li>Produkter</li><li>Kontaktpersoner</li></ul>
      </div>
      <div>
        <h4>Utbygger</h4>
        <ul><li>Hva vi kan gjøre for dere</li></ul>
      </div>
      <div>
        <h4>Operatørnett</h4>
      </div>
    </div>
  </footer>
</body>
</html>
```